Korvane Systems Website

Website design for our company: Korvane Systems.
The website should look fresh and IT focused. Please have a look at http://www.korvanesystems.example.au/ for our current design. We want something fresh and new, professional looking, in WordPress so we can easily make changes.

Industry/Entity Type

It Company

```html
<!DOCTYPE html>
<html lang="en">
<head>
<meta charset="utf-8">
<title>Korvane Systems</title>
<link rel="stylesheet" href="https://fonts.googleapis.com/css2?family=Open+Sans:wght@400;600;700&family=Arimo:wght@400;700&display=swap">
<style>
:root{
  --green:#0fa24a;
  --blue:#0a63b3;
  --band:#0b6bb5;
  --dark:#3b3b3b;
  --darkbox:#444;
  --text:#333;
  --line:#bcbcbc;
  --heroBg:#0c1a2a;
}
*{margin:0;padding:0;box-sizing:border-box}
html,body{width:952px;height:1200px;overflow:hidden;background:#fff}
body{position:relative;font-family:Arimo,Arial,sans-serif;color:var(--text)}
.abs{position:absolute}
.heading{font-family:"Open Sans",Arial,sans-serif;font-weight:600;color:var(--blue);font-size:16px}
.rule{border-bottom:1px dashed var(--line)}
.site-header{left:0;top:0;width:952px;height:92px;background:linear-gradient(#fff,#f1f1f1);border-top:2px solid var(--blue);border-bottom:1px solid #ddd}
.brand{display:flex;align-items:center;gap:8px;font-family:"Open Sans",Arial,sans-serif;font-weight:700;font-size:17px;color:var(--green);white-space:nowrap}
.brand-mark{width:22px;height:22px;background:var(--green)}
.search{left:520px;top:27px;width:147px;height:21px;border:1px solid #ccc;background:#fff;font-style:italic;font-size:10px;color:#666;padding:4px 7px}
.search svg{position:absolute;right:5px;top:4px}
.call-label{left:718px;top:22px;font-family:"Open Sans",Arial,sans-serif;font-size:9px;color:#333}
.call-number{left:717px;top:33px;font-family:"Open Sans",Arial,sans-serif;font-size:15px;color:#222}
.main-nav{left:314px;top:64px;display:flex;font-family:"Open Sans",Arial,sans-serif;font-size:11px;color:#333}
.main-nav span{padding:0 12px;border-left:1px solid #bbb;line-height:12px}
.main-nav span:first-child{border-left:none;color:var(--green)}
.hero{left:0;top:92px;width:952px;height:335px;background:var(--heroBg)}
.hero-photo{left:133px;top:92px;width:686px;height:297px;background:linear-gradient(90deg,#c9b8a8 0%,#8a6a55 30%,#3a3f47 55%,#6e7580 80%,#9aa0a6 100%)}
.hero-arrow{width:30px;height:30px;border-radius:50%;background:#222;border:2px solid #555;top:233px}
.hero-band{left:0;top:389px;width:952px;height:38px;background:var(--band);color:#fff;text-align:center;font-family:"Open Sans",Arial,sans-serif;font-size:19px;line-height:38px}
.service{width:130px;text-align:center}
.service h3{font-family:"Open Sans",Arial,sans-serif;font-size:11px;font-weight:600;color:#333;height:20px}
.service.active h3{color:var(--green)}
.service-icon{width:96px;height:96px;border-radius:50%;margin:8px auto 0;background:radial-gradient(#f7f7f7,#e3e3e3);border:2px solid #e8e8e8;display:flex;align-items:center;justify-content:center;box-shadow:0 4px 4px -2px #ccc}
.service.active .service-icon{background:#fff;border:4px solid var(--green)}
.service p{font-size:9.5px;line-height:14px;margin-top:16px;color:#333}
.divider{left:140px;top:698px;width:676px;height:1px;background:linear-gradient(90deg,transparent,#ddd,transparent)}
.about-photo{left:140px;top:759px;width:202px;height:93px;background:linear-gradient(90deg,#c8d3dc,#6d7c88 45%,#2d3138 75%,#a8b4bf)}
.about-text{left:140px;top:858px;width:203px;font-size:8.1px;line-height:12.6px;text-align:justify;letter-spacing:-.1px}
.more{font-size:9px;font-weight:700;color:var(--green)}
.quote{font-size:9px;line-height:14.6px;color:#333;width:214px}
.quote b{font-family:Georgia,serif;font-size:13px;color:#333}
.cite{font-size:8.5px;font-weight:700;color:#444;text-align:right;width:212px}
.field{left:609px;width:203px;height:20px;border:1px solid #bbb;box-shadow:inset 0 1px 2px #e3e3e3;font-style:italic;font-size:9px;color:#666;padding:4px 8px;background:#fff}
.btn{background:var(--green);color:#fff;font-family:"Open Sans",Arial,sans-serif;font-weight:600;font-size:10.5px;text-align:center;line-height:18px;height:18px}
.client{font-family:"Open Sans",Arial,sans-serif;font-weight:700;font-size:17px;color:#555}
.site-footer{left:0;top:1084px;width:952px;height:116px;background:var(--dark);border-top:3px solid #bdbdbd}
.fbox{background:var(--darkbox);border:1px solid #5a5a5a;color:#fff}
.fbox h4{font-family:"Open Sans",Arial,sans-serif;font-weight:600;font-size:10.5px;margin:6px 0 0 9px}
.footer-links{left:140px;top:1176px;font-size:8.5px;color:#fff}
.footer-links span{color:var(--green)}
.copyright{right:147px;top:1176px;font-size:8.5px;color:#fff}
.square{width:18px;height:18px}
</style>
</head>
<body>

<header class="abs site-header">
  <div class="abs brand" style="left:140px;top:36px"><span class="brand-mark"></span>Korvane Systems</div>
  <div class="abs search">search
    <svg width="11" height="11" viewBox="0 0 11 11"><circle cx="4.5" cy="4.5" r="3.5" fill="none" stroke="#888" stroke-width="1.4"/><line x1="7" y1="7" x2="10.5" y2="10.5" stroke="#888" stroke-width="1.6"/></svg>
  </div>
  <svg class="abs" style="left:688px;top:24px" width="25" height="25" viewBox="0 0 25 25"><circle cx="12.5" cy="12.5" r="11" fill="none" stroke="var(--green)" stroke-width="1.6"/><path d="M9 6c-2 1-2 3-1 6s3 6 6 7c2 1 3 0 4-1l-2-2-2 1c-2-1-3-3-4-5l1-2z" fill="var(--green)"/></svg>
  <div class="abs call-label">Call Us Today</div>
  <div class="abs call-number">555 010 4821</div>
  <nav class="abs main-nav"><span>HOME</span><span>ABOUT US</span><span>SERVICES</span><span>SUPPORT</span><span>TESTIMONIALS</span><span>CLIENTS</span><span>CONTACT US</span></nav>
</header>

<section class="abs hero"></section>
<div class="abs hero-photo" role="img" aria-label="Engineer working on a tablet beside a networking server rack"></div>
<div class="abs hero-arrow" style="left:143px"><svg width="26" height="26" viewBox="0 0 26 26"><path d="M15 7l-6 6 6 6" fill="none" stroke="#fff" stroke-width="1.6"/></svg></div>
<div class="abs hero-arrow" style="left:779px"><svg width="26" height="26" viewBox="0 0 26 26"><path d="M11 7l6 6-6 6" fill="none" stroke="#fff" stroke-width="1.6"/></svg></div>
<div class="abs hero-band">WE HAVE SPECIALISED ENGINEERS, TRAINED TO DO SPECIALISED WORK</div>

<h2 class="abs heading" style="left:142px;top:457px">Our Services</h2>
<div class="abs rule" style="left:142px;top:480px;width:672px"></div>
<svg class="abs" style="left:782px;top:465px" width="30" height="12" viewBox="0 0 30 12"><path d="M7 1l-5 5 5 5" fill="none" stroke="#777" stroke-width="1.3"/><path d="M22 1l5 5-5 5" fill="none" stroke="var(--green)" stroke-width="1.3"/></svg>

<div class="abs service active" style="left:132px;top:502px"><h3>On-site Service</h3>
  <div class="service-icon"><svg width="50" height="50" viewBox="0 0 50 50"><path d="M12 38l20-20M14 14l22 22" stroke="var(--green)" stroke-width="6" stroke-linecap="round"/><rect x="8" y="8" width="14" height="8" transform="rotate(45 15 12)" fill="var(--green)"/><circle cx="36" cy="14" r="6" fill="none" stroke="var(--green)" stroke-width="4"/></svg></div>
  <p>Lorem ipsum dolor sit amet<br>ummy nibh eui smod</p></div>
<div class="abs service" style="left:271px;top:502px"><h3>Remote Desktop</h3>
  <div class="service-icon"><svg width="50" height="50" viewBox="0 0 50 50"><rect x="6" y="10" width="28" height="20" fill="none" stroke="#555" stroke-width="3"/><line x1="14" y1="36" x2="26" y2="36" stroke="#555" stroke-width="3"/><circle cx="34" cy="30" r="10" fill="#eee" stroke="#555" stroke-width="3"/><path d="M30 30h8M35 27l3 3-3 3" fill="none" stroke="#555" stroke-width="2"/></svg></div>
  <p>Lorem ipsum dolor sit amet<br>ummy nibh eui smod</p></div>
<div class="abs service" style="left:410px;top:502px"><h3>Medical IT Service</h3>
  <div class="service-icon"><svg width="50" height="50" viewBox="0 0 50 50"><path d="M10 10v12a9 9 0 0018 0V10" fill="none" stroke="#555" stroke-width="3"/><path d="M19 31v5a8 8 0 0016 0v-6" fill="none" stroke="#555" stroke-width="3"/><circle cx="35" cy="24" r="4" fill="none" stroke="#555" stroke-width="3"/><circle cx="38" cy="12" r="5" fill="none" stroke="#555" stroke-width="2.5" stroke-dasharray="3 2"/></svg></div>
  <p>Lorem ipsum dolor sit amet<br>ummy nibh eui smod</p></div>
<div class="abs service" style="left:548px;top:502px"><h3>Pharmacy IT</h3>
  <div class="service-icon"><svg width="50" height="50" viewBox="0 0 50 50"><rect x="6" y="8" width="32" height="26" fill="none" stroke="#555" stroke-width="3"/><path d="M11 26l6-7 5 4 7-9" fill="none" stroke="#555" stroke-width="2.5"/><circle cx="34" cy="33" r="6" fill="#eee" stroke="#555" stroke-width="3"/><line x1="38" y1="37" x2="44" y2="43" stroke="#555" stroke-width="4"/></svg></div>
  <p>Lorem ipsum dolor sit amet<br>ummy nibh eui smod</p></div>
<div class="abs service" style="left:687px;top:502px"><h3>Website Design</h3>
  <div class="service-icon"><svg width="50" height="50" viewBox="0 0 50 50"><rect x="7" y="12" width="36" height="24" fill="none" stroke="#555" stroke-width="3"/><line x1="18" y1="41" x2="32" y2="41" stroke="#555" stroke-width="3"/><path d="M19 31l3-7 14-14 4 4-14 14z" fill="#555"/></svg></div>
  <p>Lorem ipsum dolor sit amet<br>ummy nibh eui smod</p></div>

<div class="abs divider"></div>

<h2 class="abs heading" style="left:140px;top:726px">About Korvane Systems</h2>
<div class="abs rule" style="left:140px;top:749px;width:204px"></div>
<div class="abs about-photo" role="img" aria-label="Team of colleagues meeting around a table"></div>
<p class="abs about-text">Korvane Systems is an Adelaide based company with a single objective - to excel in the support and service of all computer and IT needs. We provide a high level of consulting services using the most experienced engineers at a reasonable and fair price. We believe in using a Business Value approach to every</p>
<div class="abs more" style="left:288px;top:942px">Read More »</div>

<h2 class="abs heading" style="left:373px;top:726px">Client Testimonials</h2>
<div class="abs rule" style="left:373px;top:749px;width:204px"></div>
<p class="abs quote" style="left:371px;top:762px"><b>“</b> Nonummy nibh uismod tincidunt ut laoreet dolore magna aliquam erat volutpat. Ut wisi enim ad minim nonummy nibh euismod tincidunt <b>”</b></p>
<div class="abs cite" style="left:365px;top:807px">Arlen Petrov - NDT</div>
<p class="abs quote" style="left:371px;top:823px"><b>“</b> I have always found the team extremely helpful with their advice over the phone. They also have the ability to access our computers remotely, and can rectify most problems quite swiftly. I have no hesitation in recommending Korvane Systems for all of your IT needs. <b>”</b></p>
<div class="abs cite" style="left:368px;top:911px">Simon Caldreth B.Pharm<br>Westridge Family Pharmacy, Elm Park</div>
<div class="abs more" style="left:529px;top:942px">Read More »</div>

<h2 class="abs heading" style="left:608px;top:726px">Quick Contact</h2>
<div class="abs rule" style="left:608px;top:749px;width:204px"></div>
<div class="abs field" style="top:761px">Name</div>
<div class="abs field" style="top:793px">Email</div>
<div class="abs field" style="top:825px">Phone</div>
<div class="abs field" style="top:857px;height:59px">Message</div>
<div class="abs btn" style="left:611px;top:928px;width:49px">Submit</div>

<h2 class="abs heading" style="left:140px;top:978px">Our Clients</h2>
<div class="abs rule" style="left:140px;top:1003px;width:447px"></div>
<svg class="abs" style="left:556px;top:985px" width="30" height="12" viewBox="0 0 30 12"><path d="M7 1l-5 5 5 5" fill="none" stroke="#777" stroke-width="1.3"/><path d="M22 1l5 5-5 5" fill="none" stroke="var(--green)" stroke-width="1.3"/></svg>
<div class="abs client" style="left:142px;top:1025px">Halvexo</div>
<div class="abs client" style="left:280px;top:1025px;font-weight:400;color:#999">Nubrisko</div>
<div class="abs client" style="left:420px;top:1025px">Quorvel</div>
<div class="abs client" style="left:512px;top:1025px;color:#666">Zentrovy</div>

<h2 class="abs heading" style="left:604px;top:978px">Remote Support</h2>
<div class="abs rule" style="left:604px;top:1003px;width:206px"></div>
<div class="abs field" style="left:604px;top:1012px;width:201px">Enter your 6 digit code</div>
<div class="abs btn" style="left:604px;top:1040px;width:72px">Connect Now</div>

<footer class="abs site-footer"></footer>
<div class="abs fbox" style="left:140px;top:1100px;width:183px;height:56px"><h4>Subscribe to Newsletter</h4>
  <div class="abs" style="left:7px;top:28px;width:136px;height:20px;background:#595959;font-style:italic;font-size:8.5px;padding:5px 8px">Email here</div>
  <div class="abs" style="left:147px;top:28px;width:24px;height:20px;background:#595959"><svg width="24" height="20" viewBox="0 0 24 20"><path d="M10 5l5 5-5 5" fill="none" stroke="#fff" stroke-width="2.4"/></svg></div></div>
<div class="abs fbox" style="left:363px;top:1100px;width:161px;height:56px"><h4>Contact Us</h4>
  <div style="font-size:8.5px;margin:5px 0 0 9px;line-height:14px;white-space:nowrap">☎ &nbsp;555 010 4821<br>✉ &nbsp;support@korvane.example.au</div></div>
<div class="abs fbox" style="left:564px;top:1100px;width:88px;height:56px"><h4>Follow Us</h4>
  <div style="display:flex;gap:11px;margin:7px 0 0 7px"><span class="square" style="background:#3b5b98"></span><span class="square" style="background:#4aa6d6"></span><span class="square" style="background:#e8701e"></span></div></div>
<div class="abs brand" style="left:692px;top:1117px;color:#fff;font-size:14px"><span class="brand-mark"></span>Korvane Systems</div>
<div class="abs footer-links"><span>Home</span> &nbsp;|&nbsp; About Us &nbsp;|&nbsp; Services &nbsp;|&nbsp; Support &nbsp;|&nbsp; Testimonials &nbsp;|&nbsp; Clients &nbsp;|&nbsp; Contact Us &nbsp;|&nbsp; Terms Conditions</div>
<div class="abs copyright">Copyright © 2014 &nbsp;korvanesystems. &nbsp;All Rights Reserved</div>

</body>
</html>
```